Best Seller Book Cover ...

Book Title: Skip the Big Answer: Pick a Trail, Keep to That Trail, Mind the Geese

Edgy, Minimalist, Compelling, Attractive, Classy design.

Very clean. See examples.,

Target Market(s)

Mid Life People ages 38-55 Male and Female equally

• Nice to Have:

Minimalist and eye catching ( i have loaded a few examples of what this means)
Should not have
• Clip Art
Clutter

```html
<!DOCTYPE html>
<html lang="en">
<head>
<meta charset="utf-8">
<title>Skip the Big Answer — Book Cover</title>
<link rel="stylesheet" href="https://fonts.googleapis.com/css2?family=Anton&display=swap">
<style>
  :root {
    --stage: #e9e4dc;
    --parchment-light: #b89a74;
    --parchment-mid: #9a7b58;
    --parchment-dark: #6e533a;
    --ink: #1f1a17;
    --ember: #d9822b;
    --ember-soft: #f0b060;
    --glow: #f7e6c4;
  }
  * { margin: 0; padding: 0; box-sizing: border-box; }
  html, body {
    width: 1200px;
    height: 800px;
    overflow: hidden;
    background: var(--stage);
  }
  .canvas {
    position: relative;
    width: 1200px;
    height: 800px;
    display: flex;
    align-items: center;
    justify-content: center;
  }
  .cover {
    position: relative;
    width: 520px;
    height: 744px;
    overflow: hidden;
    background:
      radial-gradient(ellipse at 50% 35%, var(--parchment-light) 0%, var(--parchment-mid) 55%, var(--parchment-dark) 100%);
    box-shadow: 0 4px 18px rgba(0,0,0,0.25);
  }
  .cover__glow {
    position: absolute;
    top: 110px;
    width: 150px;
    height: 120px;
    background: radial-gradient(ellipse at center, rgba(247,230,196,0.85) 0%, rgba(247,230,196,0.25) 45%, rgba(247,230,196,0) 72%);
  }
  .cover__glow--left { left: 50px; }
  .cover__glow--right { right: 40px; }
  .cover__beam {
    position: absolute;
    left: 252px;
    top: 260px;
    width: 24px;
    height: 484px;
  }
  .title {
    position: absolute;
    top: 118px;
    left: 110px;
    width: 320px;
    padding: 14px 16px 16px;
    text-align: left;
    font-family: "Anton", "Arial Narrow", sans-serif;
    color: var(--ink);
    background: radial-gradient(ellipse at center, rgba(240,176,96,0.55) 0%, rgba(217,130,43,0.35) 60%, rgba(217,130,43,0) 100%);
    border-radius: 18px;
  }
  .title__main {
    line-height: 1.02;
    text-shadow: 0 0 6px var(--ember), 0 0 2px var(--ember-soft);
  }
  .title__line { display: block; }
  .title__big { font-size: 44px; letter-spacing: 0.5px; }
  .title__small { font-size: 32px; }
  .title__sub {
    display: block;
    margin-top: 8px;
    font-size: 14px;
    line-height: 1.25;
    letter-spacing: 1px;
    text-shadow: 0 0 5px var(--ember);
  }
</style>
</head>
<body>
  <main class="canvas">
    <section class="cover" aria-label="Book cover">
      <div class="cover__glow cover__glow--left" role="img" aria-label="Soft glowing wisp of light"></div>
      <div class="cover__glow cover__glow--right" role="img" aria-label="Soft glowing wisp of light"></div>
      <svg class="cover__beam" viewBox="0 0 24 484" preserveAspectRatio="none" aria-hidden="true">
        <defs>
          <linearGradient id="beamFade" x1="0" y1="0" x2="0" y2="1">
            <stop offset="0" stop-color="#f7e6c4" stop-opacity="1"/>
            <stop offset="0.6" stop-color="#f0c98c" stop-opacity="0.8"/>
            <stop offset="1" stop-color="#d9a060" stop-opacity="0.5"/>
          </linearGradient>
          <linearGradient id="beamSide" x1="0" y1="0" x2="1" y2="0">
            <stop offset="0" stop-color="#f7e6c4" stop-opacity="0"/>
            <stop offset="0.5" stop-color="#f7e6c4" stop-opacity="0.6"/>
            <stop offset="1" stop-color="#f7e6c4" stop-opacity="0"/>
          </linearGradient>
        </defs>
        <rect x="0" y="0" width="24" height="484" fill="url(#beamSide)"/>
        <path d="M12 0 L15 484 L9 484 Z" fill="url(#beamFade)"/>
      </svg>
      <h1 class="title">
        <span class="title__main">
          <span class="title__line"><span class="title__big">SKIP</span> <span class="title__small">THE</span></span>
          <span class="title__line title__big">BIG ANSWER:</span>
        </span>
        <span class="title__sub">PICK A TRAIL, KEEP TO THAT TRAIL,<br>MIND THE GEESE</span>
      </h1>
    </section>
  </main>
</body>
</html>
```